Building technology company seek stationery design and folder design

Letterhead, and a folder design
ideally, I would have two letter head design, one is for one-page bussiness letter. the other one I can use for longer document such report, or analysis regular report page
you can find company logo and overall style at our website:
www.plinthcove.example

we are in building technology business, using internet of things technology to improve building energy efficiency to make building greener.

Industry/Entity Type

It Company

Requirements
Must have
• company logo
Nice to have
• techy look abstract graphics, etc.
Should not have
• no comment

```html
<!DOCTYPE html>
<html lang="en">
<head>
<meta charset="utf-8">
<title>Plinth Cove Letterhead</title>
<link href="https://fonts.googleapis.com/css2?family=Roboto:wght@400;500&display=swap" rel="stylesheet">
<style>
  :root {
    --backdrop: #e4e4e8;
    --paper: #ffffff;
    --brand-green: #8cc63f;
    --ink-grey: #5a5a5a;
    --rule-grey: #9a9a9a;
    --skyline-tint: #f1f1ef;
  }
  html, body {
    margin: 0;
    padding: 0;
    width: 1200px;
    height: 992px;
    overflow: hidden;
    background: var(--backdrop);
    font-family: "Roboto", Arial, sans-serif;
  }
  .letterhead {
    position: absolute;
    left: 240px;
    top: 10px;
    width: 720px;
    height: 972px;
    background: var(--paper);
    box-shadow: 0 2px 8px rgba(0,0,0,0.12);
  }
  .brand {
    position: absolute;
    left: 58px;
    top: 72px;
    display: flex;
    align-items: center;
    gap: 10px;
  }
  .brand-mark {
    width: 22px;
    height: 22px;
    background: var(--brand-green);
  }
  .brand-name {
    font-size: 26px;
    font-weight: 500;
    letter-spacing: 2px;
    color: var(--ink-grey);
    text-transform: uppercase;
  }
  .contact-block {
    position: absolute;
    left: 522px;
    top: 66px;
    padding-left: 14px;
    border-left: 1px solid var(--rule-grey);
    display: flex;
    flex-direction: column;
    gap: 4px;
  }
  .contact-line {
    display: flex;
    align-items: center;
    gap: 6px;
    font-size: 10.5px;
    line-height: 12px;
    color: var(--ink-grey);
  }
  .contact-icon {
    width: 9px;
    height: 9px;
    fill: var(--brand-green);
    stroke: var(--brand-green);
  }
  .skyline-band {
    position: absolute;
    left: 9px;
    right: 5px;
    bottom: 0;
    height: 145px;
    background: linear-gradient(to bottom, rgba(241,241,239,0) 0%, var(--skyline-tint) 25%, var(--skyline-tint) 100%);
  }
</style>
</head>
<body>
  <main class="letterhead">
    <header>
      <div class="brand">
        <span class="brand-mark"></span>
        <span class="brand-name">Plinth Cove</span>
      </div>
      <address class="contact-block" style="font-style:normal">
        <div class="contact-line">
          <svg class="contact-icon" viewBox="0 0 10 10"><path d="M2 0.5 L3.6 2.6 L2.8 3.6 Q4 6 6.4 7.2 L7.4 6.4 L9.5 8 L8.4 9.5 Q3 9 0.5 1.6 Z" stroke="none"/></svg>
          <span>(555) 014-2286</span>
        </div>
        <div class="contact-line">
          <svg class="contact-icon" viewBox="0 0 10 10"><rect x="0.5" y="2" width="9" height="6" stroke="none"/><path d="M0.8 2.3 L5 5.5 L9.2 2.3" fill="none" stroke="#fff" stroke-width="0.9"/></svg>
          <span>info@plinthcove.example</span>
        </div>
        <div class="contact-line">
          <svg class="contact-icon" viewBox="0 0 10 10" fill="none" stroke-width="0.9"><circle cx="5" cy="5" r="4.3"/><ellipse cx="5" cy="5" rx="1.9" ry="4.3"/><path d="M0.7 5 H9.3"/></svg>
          <span>www.plinthcove.example</span>
        </div>
      </address>
    </header>
    <div class="skyline-band" role="img" aria-label="Faint pale grey city skyline silhouette along the bottom of the page"></div>
  </main>
</body>
</html>
```